Business Card for Yachting Management Company

Need a business card design for a new yachting project management company. Attached is the logo for the company.
Our clients are large yacht owners and captains.
Design must be in the style of the logo. Modern, elegant.

Example of data to show:
Peter Hollis
Project Manager
(+34) 612 738 104
peter@quorvane.net
Quorvane Management - Meridel Tower, Office 22 - KRB - Palma de Mallorca

The data above will have to be changed (by me) for the different people in the company over the next years.

Will be printed using PrintNova (Lustre Card Series). They provide these guidelines for the size:
"the actual size of the card is 1050 x 600 pixels. However, the full bleed size is 1083 x 633 pixels, and the safe printing area is 1008 x 558 pixels."

```html
<!DOCTYPE html>
<html lang="en">
<head>
<meta charset="utf-8">
<title>Quorvane Management – Business Card</title>
<link href="https://fonts.googleapis.com/css2?family=Open+Sans:wght@300;400;700&display=swap" rel="stylesheet">
<style>
  :root {
    --backdrop: #d8d8d8;
    --card-white: #ffffff;
    --card-black: #1a1a1a;
    --brand-blue: #1a6fc9;
    --text-grey: #8c8c8c;
    --rule-grey: #c4c4c4;
  }
  * { margin: 0; padding: 0; box-sizing: border-box; }
  html, body {
    width: 1200px;
    height: 846px;
    overflow: hidden;
    background: var(--backdrop);
    font-family: "Open Sans", Arial, sans-serif;
  }
  .canvas {
    position: relative;
    width: 1200px;
    height: 846px;
  }
  .card {
    position: absolute;
    top: 268px;
    width: 540px;
    height: 309px;
    box-shadow: 0 6px 18px rgba(0,0,0,0.12);
  }
  .card--front { left: 40px; background: var(--card-white); }
  .card--back  { left: 620px; background: var(--card-black); }

  .front-row {
    position: absolute;
    left: 36px;
    right: 24px;
    top: 148px;
    display: flex;
    align-items: center;
  }
  .wordmark {
    color: var(--brand-blue);
    font-weight: 700;
    font-size: 15px;
    line-height: 1.2;
    width: 120px;
  }
  .divider {
    width: 1px;
    height: 72px;
    background: var(--rule-grey);
    margin: 0 16px;
  }
  .contact-block p {
    font-size: 12px;
    font-weight: 300;
    color: var(--text-grey);
    line-height: 1.45;
    white-space: nowrap;
  }
  .contact-block .contact-heading {
    font-size: 13px;
    font-weight: 700;
    color: var(--brand-blue);
  }

  .back-wordmark {
    position: absolute;
    inset: 0;
    display: flex;
    align-items: center;
    justify-content: center;
    color: var(--brand-blue);
    font-weight: 700;
    font-size: 34px;
    letter-spacing: 0.5px;
  }
</style>
</head>
<body>
<main class="canvas">
  <section class="card card--front" aria-label="Card front">
    <div class="front-row">
      <div class="wordmark">Quorvane Management</div>
      <div class="divider"></div>
      <div class="contact-block">
        <p class="contact-heading">Peter Hollis</p>
        <p>Project Manager</p>
        <p>(+34) 612 738 104</p>
        <p>peter@quorvane.net</p>
      </div>
      <div class="divider"></div>
      <div class="contact-block">
        <p class="contact-heading">Quorvane Management</p>
        <p>Meridel Tower</p>
        <p>Office 22 - KRB</p>
        <p>Palma de Mallorca</p>
      </div>
    </div>
  </section>

  <section class="card card--back" aria-label="Card back">
    <div class="back-wordmark">Quorvane Management</div>
  </section>
</main>
</body>
</html>
```